UI Improvement for FlorQuay app

We are looking for a talented UI/UX designer to REFINE and enhance the visual design of our mobile application, FlorQuay. The app is fully functional, but we need a designer to improve its aesthetics by specifying design elements such as fonts, colors, spacing, and component styles.
Your task will be to analyze the CURRENT UI and provide detailed design specifications that will make the app more visually appealing, modern, and user-friendly.
TODO:
Review the existing FlorQuay app design (see attachments) and identify areas for visual improvement.
Provide a detailed UI style guide, including:
Typography (font choices, sizes, and weights)
Color palette (primary, secondary, and accent colors)
Component styling (buttons, forms, icons, and interactive elements)
Spacing and layout guidelines (margins, paddings, and alignment)
Ensure the design remains clean, modern, and professional while maintaining usability and accessibility.
Provide design mockups or visual examples (if possible) to illustrate the proposed changes.
Deliverables:
A UI Style Guide (PDF or Figma file) with specifications on fonts, colors, spacing, and UI components.
Optionally, before/after mockups or examples demonstrating the improvements.
Ideal Designer:
Strong experience in mobile UI/UX design.
Understanding of modern design trends and best practices.
Ability to communicate design choices clearly for easy developer implementation.
I have attached 7 images showcasing the main UI screens used in the FlorQuay app. These screens need visual enhancements to improve their overall look and user experience.
The images represent the current design in three key modes:
LIST Mode – Displays data in a structured list format.
READ Mode – Shows detailed information when a user selects an item.
ADD/EDIT Mode – Allows users to input or modify information.
Additionally, there is a ‘MORE’ page, which serves as a menu listing other features of the application.
Task Objective:
Please refine and improve these UIs to create a more modern, visually appealing, and user-friendly experience. Focus on typography, colors, spacing, and component styling to ensure a cohesive and polished design.
Look and feel
Each slider illustrates characteristics of the customer's brand and the style your logo design should communicate.

```html
<!DOCTYPE html>
<html lang="en">
<head>
<meta charset="utf-8">
<title>FlorQuay – Contact and Pilots screens</title>
<link rel="stylesheet" href="https://fonts.googleapis.com/css2?family=Roboto:wght@400;500;700&display=swap">
<style>
:root{
  --bg-top:#03a88f;
  --bg-bottom:#0a55ad;
  --brand-blue:#0b4ea9;
  --brand-blue-dark:#083f8c;
  --brand-green:#08a586;
  --accent-green:#1bb36b;
  --surface:#f2f2f2;
  --surface-dark:#dcdcdc;
  --card:#efefef;
  --field:#ffffff;
  --text:#2b2b2b;
  --muted:#666;
  --white:#fff;
}
*{box-sizing:border-box;margin:0;padding:0}
html,body{width:1200px;height:781px;overflow:hidden}
body{
  font-family:"Roboto",Arial,sans-serif;
  background:linear-gradient(180deg,var(--bg-top) 0%,var(--bg-bottom) 100%);
  position:relative;color:var(--text);
}
.screen{
  position:absolute;top:100px;width:265px;height:575px;border-radius:24px;overflow:hidden;
  background:linear-gradient(180deg,var(--surface) 0%,var(--surface-dark) 100%);
  box-shadow:0 6px 18px rgba(0,0,0,.18);
}
.screen--edit{left:78px}
.screen--list{left:468px}
.screen--read{left:858px}

.app-header{position:absolute;left:0;top:0;width:100%;height:78px;background:var(--brand-blue);color:var(--white)}
.status-time{position:absolute;left:16px;top:11px;font-size:9.5px;font-weight:700}
.status-icons{position:absolute;right:18px;top:10px;display:flex;gap:6px;align-items:center}
.back-btn{position:absolute;left:18px;top:38px;width:24px;height:24px;border-radius:50%;background:var(--brand-green);display:flex;align-items:center;justify-content:center}
.app-title{position:absolute;left:0;right:0;top:39px;text-align:center;font-size:17px;font-weight:700}
.save-btn{position:absolute;right:16px;top:39px;height:20px;padding:0 10px;background:var(--brand-blue-dark);border-radius:2px;font-size:10px;font-weight:700;line-height:20px}
.add-btn{position:absolute;right:16px;top:38px;font-size:16px;font-weight:400;line-height:22px}

.app-body{position:absolute;left:0;top:78px;right:0;bottom:39px}
.card{position:absolute;left:17px;width:231px;background:var(--card);border-radius:10px;box-shadow:0 0 0 1px rgba(255,255,255,.6)}

.field-label{display:block;font-size:8.5px;color:var(--text);margin-bottom:4px}
.field{height:29px;background:var(--field);border-radius:4px;box-shadow:0 1px 2px rgba(0,0,0,.06);margin-bottom:9px}
.form-card{padding:12px 12px 4px}
.field-row{display:flex;gap:5px}
.field-row .col{flex:1}
.field-row .field{margin-bottom:0}

.search-label{position:absolute;left:28px;top:15px;font-size:8.5px}
.search-box{position:absolute;left:28px;top:27px;width:206px;height:29px;background:var(--field);border-radius:3px}
.search-btn{position:absolute;right:3px;top:3px;width:22px;height:22px;background:var(--brand-blue);border-radius:3px;display:flex;align-items:center;justify-content:center}
.pilot-list{top:67px;height:376px;left:16px;width:232px;padding:14px 0 0 16px}
.pilot{display:flex;align-items:center;height:51px}
.avatar{width:36px;height:36px;border-radius:50%;border:2px solid var(--white);box-shadow:0 0 0 1.5px var(--av);background:var(--av);color:var(--white);font-size:14px;font-weight:700;display:flex;align-items:center;justify-content:center;margin-right:7px;flex:none}
.pilot-name{font-size:10px;color:var(--text);white-space:nowrap}
.pilot-date{display:inline-block;margin-top:3px;background:var(--accent-green);color:var(--white);font-size:8.5px;padding:1px 6px;border-radius:2px}

.actions-card{top:13px;height:264px;padding:12px 0 0 12px}
.action{display:flex;align-items:center;width:206px;height:29px;background:var(--field);border-radius:3px;margin-bottom:6.5px;padding-left:8px;font-size:8.5px}
.plus-dot{width:15px;height:15px;border-radius:50%;background:var(--brand-blue);color:var(--white);font-size:10px;line-height:15px;text-align:center;margin-right:7px}
.related-card{top:284px;height:260px;padding:10px 0 0 12px}
.panel{width:206px;border-radius:3px;padding:9px 12px;color:var(--white);margin-bottom:9px}
.panel--green{background:var(--brand-green);height:62px}
.panel--blue{background:var(--brand-blue);height:76px}
.panel-head{display:flex;justify-content:space-between;font-size:8.5px;margin-bottom:6px}
.panel-head strong{font-weight:700}
.select{position:relative;background:var(--field);border-radius:3px;color:var(--muted);font-size:7px;line-height:10.5px;padding:5px 26px 5px 6px;min-height:22px}
.select-caret{position:absolute;right:5px;top:5px;width:13px;height:13px;border-radius:50%;background:#e4e4e4;display:flex;align-items:center;justify-content:center}

.tab-bar{position:absolute;left:0;right:0;bottom:0;height:39px;background:var(--brand-green);display:flex;align-items:center;justify-content:space-around;padding:0 8px}
.tab{width:24px;height:24px;display:flex;align-items:center;justify-content:center}
.tab--active{background:var(--white);border-radius:50%}
</style>
</head>
<body>

<!-- Add / edit contact -->
<section class="screen screen--edit">
  <header class="app-header">
    <span class="status-time">9.41</span>
    <span class="status-icons">
      <svg width="11" height="8" viewBox="0 0 11 8"><path d="M1 3a6.5 6.5 0 0 1 9 0M2.8 4.8a4 4 0 0 1 5.4 0" stroke="#fff" stroke-width="1.2" fill="none"/><circle cx="5.5" cy="6.8" r="1" fill="#fff"/></svg>
      <svg width="13" height="7" viewBox="0 0 13 7"><rect x=".5" y=".5" width="10.5" height="6" rx="1" stroke="#fff" fill="none"/><rect x="2" y="2" width="7" height="3" fill="#fff"/><rect x="11.5" y="2.3" width="1.2" height="2.4" fill="#fff"/></svg>
    </span>
    <span class="back-btn"><svg width="8" height="10" viewBox="0 0 8 10"><path d="M5.5 1.5 2 5l3.5 3.5" stroke="#fff" stroke-width="1.4" fill="none"/></svg></span>
    <h1 class="app-title">Contact</h1>
    <span class="save-btn">Save</span>
  </header>
  <main class="app-body">
    <div class="card form-card" style="top:16px;height:221px">
      <label class="field-label">Business name</label><div class="field"></div>
      <label class="field-label">First name</label><div class="field"></div>
      <label class="field-label">Middle name</label><div class="field"></div>
      <label class="field-label">Last name</label><div class="field"></div>
    </div>
    <div class="card form-card" style="top:247px;height:230px">
      <label class="field-label">Address Lable</label><div class="field"></div>
      <label class="field-label">Address Line 1</label><div class="field"></div>
      <label class="field-label">Address Line 2</label><div class="field"></div>
      <div class="field-row">
        <div class="col"><label class="field-label">City</label><div class="field"></div></div>
        <div class="col"><label class="field-label">State</label><div class="field"></div></div>
        <div class="col"><label class="field-label">Zip</label><div class="field"></div></div>
      </div>
    </div>
  </main>
  <nav class="tab-bar">
    <span class="tab tab--active"><svg width="14" height="14" viewBox="0 0 24 24"><path d="M6.6 10.8a15 15 0 0 0 6.6 6.6l2.2-2.2a1 1 0 0 1 1-.25 11 11 0 0 0 3.6.6 1 1 0 0 1 1 1V20a1 1 0 0 1-1 1A17 17 0 0 1 3 4a1 1 0 0 1 1-1h3.5a1 1 0 0 1 1 1 11 11 0 0 0 .6 3.6 1 1 0 0 1-.25 1z" fill="#0b4ea9"/></svg></span>
    <span class="tab"><svg width="16" height="14" viewBox="0 0 16 14"><ellipse cx="6" cy="5.5" rx="5.5" ry="4.5" fill="#fff"/><ellipse cx="10.5" cy="8.5" rx="5" ry="4" fill="#fff" stroke="#08a586"/><circle cx="8.5" cy="8.5" r=".8" fill="#08a586"/><circle cx="10.5" cy="8.5" r=".8" fill="#08a586"/><circle cx="12.5" cy="8.5" r=".8" fill="#08a586"/></svg></span>
    <span class="tab"><svg width="17" height="13" viewBox="0 0 17 13"><rect x="5.5" y=".8" width="6" height="3" rx="1" stroke="#fff" fill="none" stroke-width="1.3"/><rect x=".5" y="3" width="16" height="9.5" rx="1.5" fill="#fff"/><rect x=".5" y="6.6" width="16" height="1.2" fill="#08a586"/></svg></span>
    <span class="tab"><svg width="12" height="15" viewBox="0 0 12 15"><rect width="12" height="15" rx="1.5" fill="#fff"/><path d="M3 4h6M3 7h6M3 10h4" stroke="#08a586" stroke-width="1.2"/></svg></span>
    <span class="tab"><svg width="15" height="15" viewBox="0 0 15 15"><rect width="6.5" height="6.5" rx="1.5" fill="#fff"/><rect x="8.5" width="6.5" height="6.5" rx="1.5" fill="#fff"/><rect y="8.5" width="6.5" height="6.5" rx="1.5" fill="#fff"/><rect x="8.5" y="8.5" width="6.5" height="6.5" rx="1.5" fill="#fff"/></svg></span>
  </nav>
</section>

<!-- Pilots list -->
<section class="screen screen--list">
  <header class="app-header">
    <span class="status-time">9.41</span>
    <span class="status-icons">
      <svg width="11" height="8" viewBox="0 0 11 8"><path d="M1 3a6.5 6.5 0 0 1 9 0M2.8 4.8a4 4 0 0 1 5.4 0" stroke="#fff" stroke-width="1.2" fill="none"/><circle cx="5.5" cy="6.8" r="1" fill="#fff"/></svg>
      <svg width="13" height="7" viewBox="0 0 13 7"><rect x=".5" y=".5" width="10.5" height="6" rx="1" stroke="#fff" fill="none"/><rect x="2" y="2" width="7" height="3" fill="#fff"/><rect x="11.5" y="2.3" width="1.2" height="2.4" fill="#fff"/></svg>
    </span>
    <span class="back-btn"><svg width="8" height="10" viewBox="0 0 8 10"><path d="M5.5 1.5 2 5l3.5 3.5" stroke="#fff" stroke-width="1.4" fill="none"/></svg></span>
    <h1 class="app-title">Pilots</h1>
    <span class="add-btn">+</span>
  </header>
  <main class="app-body">
    <span class="search-label">Search</span>
    <div class="search-box"><span class="search-btn"><svg width="9" height="9" viewBox="0 0 9 9"><circle cx="3.7" cy="3.7" r="2.7" stroke="#fff" stroke-width="1.3" fill="none"/><path d="M5.8 5.8 8.3 8.3" stroke="#fff" stroke-width="1.4"/></svg></span></div>
    <div class="card pilot-list">
      <div class="pilot"><span class="avatar" style="--av:#0b4ea9">A</span><div><div class="pilot-name">Archer, Lena, Marie, 5720418</div><span class="pilot-date">30 Sep 2024</span></div></div>
      <div class="pilot"><span class="avatar" style="--av:#7cc242">B</span><div><div class="pilot-name">Bexley, Howard, 6093274</div><span class="pilot-date">28 Feb 2024</span></div></div>
      <div class="pilot"><span class="avatar" style="--av:#444">B</span><div><div class="pilot-name">Brandt, Oliver, 7148309</div><span class="pilot-date">30 Oct 2024</span></div></div>
      <div class="pilot"><span class="avatar" style="--av:#cf62e0">C</span><div><div class="pilot-name">Corwin, Mia, Celeste, 8261950</div><span class="pilot-date">30 Mar 2024</span></div></div>
      <div class="pilot"><span class="avatar" style="--av:#0b4ea9">C</span><div><div class="pilot-name">Castell Ruiz, Tomas, Elena</div><span class="pilot-date">30 Sep 2024</span></div></div>
      <div class="pilot"><span class="avatar" style="--av:#14a84a">G</span><div><div class="pilot-name">Grafton, Dale, 9035762</div><span class="pilot-date">28 Feb 2025</span></div></div>
      <div class="pilot"><span class="avatar" style="--av:#f39224">G</span><div><div class="pilot-name">Gilmore, Peter, Alan, 1874206</div><span class="pilot-date">06 Mar 2023</span></div></div>
    </div>
  </main>
  <nav class="tab-bar">
    <span class="tab tab--active"><svg width="14" height="14" viewBox="0 0 24 24"><path d="M6.6 10.8a15 15 0 0 0 6.6 6.6l2.2-2.2a1 1 0 0 1 1-.25 11 11 0 0 0 3.6.6 1 1 0 0 1 1 1V20a1 1 0 0 1-1 1A17 17 0 0 1 3 4a1 1 0 0 1 1-1h3.5a1 1 0 0 1 1 1 11 11 0 0 0 .6 3.6 1 1 0 0 1-.25 1z" fill="#0b4ea9"/></svg></span>
    <span class="tab"><svg width="16" height="14" viewBox="0 0 16 14"><ellipse cx="6" cy="5.5" rx="5.5" ry="4.5" fill="#fff"/><ellipse cx="10.5" cy="8.5" rx="5" ry="4" fill="#fff" stroke="#08a586"/><circle cx="8.5" cy="8.5" r=".8" fill="#08a586"/><circle cx="10.5" cy="8.5" r=".8" fill="#08a586"/><circle cx="12.5" cy="8.5" r=".8" fill="#08a586"/></svg></span>
    <span class="tab"><svg width="17" height="13" viewBox="0 0 17 13"><rect x="5.5" y=".8" width="6" height="3" rx="1" stroke="#fff" fill="none" stroke-width="1.3"/><rect x=".5" y="3" width="16" height="9.5" rx="1.5" fill="#fff"/><rect x=".5" y="6.6" width="16" height="1.2" fill="#08a586"/></svg></span>
    <span class="tab"><svg width="12" height="15" viewBox="0 0 12 15"><rect width="12" height="15" rx="1.5" fill="#fff"/><path d="M3 4h6M3 7h6M3 10h4" stroke="#08a586" stroke-width="1.2"/></svg></span>
    <span class="tab"><svg width="15" height="15" viewBox="0 0 15 15"><rect width="6.5" height="6.5" rx="1.5" fill="#fff"/><rect x="8.5" width="6.5" height="6.5" rx="1.5" fill="#fff"/><rect y="8.5" width="6.5" height="6.5" rx="1.5" fill="#fff"/><rect x="8.5" y="8.5" width="6.5" height="6.5" rx="1.5" fill="#fff"/></svg></span>
  </nav>
</section>

<!-- Contact detail -->
<section class="screen screen--read">
  <header class="app-header">
    <span class="status-time">9.41</span>
    <span class="status-icons">
      <svg width="11" height="8" viewBox="0 0 11 8"><path d="M1 3a6.5 6.5 0 0 1 9 0M2.8 4.8a4 4 0 0 1 5.4 0" stroke="#fff" stroke-width="1.2" fill="none"/><circle cx="5.5" cy="6.8" r="1" fill="#fff"/></svg>
      <svg width="13" height="7" viewBox="0 0 13 7"><rect x=".5" y=".5" width="10.5" height="6" rx="1" stroke="#fff" fill="none"/><rect x="2" y="2" width="7" height="3" fill="#fff"/><rect x="11.5" y="2.3" width="1.2" height="2.4" fill="#fff"/></svg>
    </span>
    <span class="back-btn"><svg width="8" height="10" viewBox="0 0 8 10"><path d="M5.5 1.5 2 5l3.5 3.5" stroke="#fff" stroke-width="1.4" fill="none"/></svg></span>
    <h1 class="app-title">Contact</h1>
    <span class="add-btn">+</span>
  </header>
  <main class="app-body">
    <div class="card actions-card">
      <div class="action"><span class="plus-dot">+</span>Add Email -e</div>
      <div class="action"><span class="plus-dot">+</span>Add Social Media -e</div>
      <div class="action"><span class="plus-dot">+</span>Add Emergency Contact -e</div>
      <div class="action"><span class="plus-dot">+</span>Add Personal Information -e</div>
      <div class="action"><span class="plus-dot">+</span>Add Work Info -e</div>
      <div class="action"><span class="plus-dot">+</span>Add Skills/Talents -e</div>
      <div class="action"><span class="plus-dot">+</span>Add Resources -e</div>
    </div>
    <div class="card related-card">
      <div class="panel panel--green">
        <div class="panel-head"><strong>Pilots-e</strong><span>Collapse</span></div>
        <div class="select">Ashby, Grant, 5319087, 10/31/23<span class="select-caret"><svg width="5" height="3" viewBox="0 0 5 3"><path d="M0 0h5L2.5 3z" fill="#333"/></svg></span></div>
      </div>
      <div class="panel panel--blue">
        <div class="panel-head"><strong>Aircraft Owner-e</strong><span>Collapse</span></div>
        <div class="select">Personal: Ashby, Grant: Aerlin: K7L: Aerlin AircraftCompany, Single Engine, 1100<span class="select-caret"><svg width="5" height="3" viewBox="0 0 5 3"><path d="M0 0h5L2.5 3z" fill="#333"/></svg></span></div>
      </div>
    </div>
  </main>
  <nav class="tab-bar">
    <span class="tab tab--active"><svg width="14" height="14" viewBox="0 0 24 24"><path d="M6.6 10.8a15 15 0 0 0 6.6 6.6l2.2-2.2a1 1 0 0 1 1-.25 11 11 0 0 0 3.6.6 1 1 0 0 1 1 1V20a1 1 0 0 1-1 1A17 17 0 0 1 3 4a1 1 0 0 1 1-1h3.5a1 1 0 0 1 1 1 11 11 0 0 0 .6 3.6 1 1 0 0 1-.25 1z" fill="#0b4ea9"/></svg></span>
    <span class="tab"><svg width="16" height="14" viewBox="0 0 16 14"><ellipse cx="6" cy="5.5" rx="5.5" ry="4.5" fill="#fff"/><ellipse cx="10.5" cy="8.5" rx="5" ry="4" fill="#fff" stroke="#08a586"/><circle cx="8.5" cy="8.5" r=".8" fill="#08a586"/><circle cx="10.5" cy="8.5" r=".8" fill="#08a586"/><circle cx="12.5" cy="8.5" r=".8" fill="#08a586"/></svg></span>
    <span class="tab"><svg width="17" height="13" viewBox="0 0 17 13"><rect x="5.5" y=".8" width="6" height="3" rx="1" stroke="#fff" fill="none" stroke-width="1.3"/><rect x=".5" y="3" width="16" height="9.5" rx="1.5" fill="#fff"/><rect x=".5" y="6.6" width="16" height="1.2" fill="#08a586"/></svg></span>
    <span class="tab"><svg width="12" height="15" viewBox="0 0 12 15"><rect width="12" height="15" rx="1.5" fill="#fff"/><path d="M3 4h6M3 7h6M3 10h4" stroke="#08a586" stroke-width="1.2"/></svg></span>
    <span class="tab"><svg width="15" height="15" viewBox="0 0 15 15"><rect width="6.5" height="6.5" rx="1.5" fill="#fff"/><rect x="8.5" width="6.5" height="6.5" rx="1.5" fill="#fff"/><rect y="8.5" width="6.5" height="6.5" rx="1.5" fill="#fff"/><rect x="8.5" y="8.5" width="6.5" height="6.5" rx="1.5" fill="#fff"/></svg></span>
  </nav>
</section>

</body>
</html>
```